Jewelry store needs fully functional Ecommerce website

Web Design Brief for our E-commerce Jewelry retail store.
Description

We need a fully coded Shopify website. The Shopify site will need to be fully functional with an Ecommerce integration (fully integrated with Paypal and All other gateways) and will need to be SEO optimized.
We sell jewelry items like: rings, earrings, necklaces etc. The website should have an elegant, modern, professional, fun, look.

***We would like the website to look and function similarly to this website:
https://velvorisco.com

Color Preference
Colors to be used are white background with black font and light pink/ purple/ gold tints. We have attached our logo as reference.

Functionalities
The store will function like a typical Ecommerce jewelry store, using the products/categories as the starting page. Going into individual product pages by selecting images and leading to a detailed “buy now” page for the selected product.

Target Market
Jewelry lovers.

Should Not Have:
- - Dull and common design
- - Messy/unstructured navigation

Coded - Design and coding required
Target Audience are women from 16-50 years old.
We will need to be able to add products and make modifications to the website as needed.

We need the following apps installed and Operating:
-Tally Shift; Order Look Up (rename “track your order”) ; Help Center (Questions and Answers) ; Pemmo Reviews; TXT Nudge; Drenoza Email Marketing ; Plivet (Facebook messenger bump) ; Vantro multi- currency (translate currency to buyer) ; Discounted Upsell ; Easy Contact form App
We will need all products imported: (below is information for importing products). We will provide all links that serve entire active item product catalog in shopifys import format:
DataFeed:

If you are getting started with Shopify, a combination of the Shopify Import Format and XML feeds is ideal. The Shopify Import Format will output a file that can be uploaded into Shopify’s product database. After you import, you can use the XML feed and a third party app to keep the inventory up to date in real time, take down items that go out of stock etc., all without regular human intervention. There a several Shopify apps that can do this type of feed integration. We have had a good experience with Tally Shift, which is an app that can be configured to accept our XML feed and update products on a set schedule. You can even set your own margins based on our wholesale price with this app.

Shopify Formatted HTML TableTo make it easier to get started on Shopify, we included a format that outputs the required fields for a product import in Shopify. In order to use the embedded Excel file, first open the file (Auto-Shopify-Datasheet-Format.xslx), Refresh it (under Data tab), and then Save As with a new file name in a CSV (UTF-8) file. That file can then be split into smaller CSV files (if there is a limit on the number of products per file) for import into Shopify.

Target Market(s)

Jewelry Lovers

Industry/Entity Type

Jewelry Store

Coding

Number of Pages Required

5+ page

Colors
eda3c7
d3a5cc
ffffff

Requirements
Must have
• Color Preference
Colors to be used are white background with black font and light pink/ purple/ gold tints.

https://velvorisco.com
Should not have
• Should Not Have:

```html
<!DOCTYPE html>
<html lang="en">
<head>
<meta charset="utf-8">
<title>Lumen Vale – Shop Now</title>
<link href="https://fonts.googleapis.com/css2?family=Alegreya:wght@400;500;700&family=Alegreya+SC:wght@400;500&family=Montserrat:wght@400&display=swap" rel="stylesheet">
<style>
:root{
  --pink:#eda3c7;
  --lilac:#d3a5cc;
  --btn:#d8a8d0;
  --ink:#1b1b1b;
  --muted:#777;
  --line:#cfcfcf;
  --dark:#0e1113;
  --white:#ffffff;
}
*{margin:0;padding:0;box-sizing:border-box}
html,body{width:1200px;height:3158px;overflow:hidden;background:var(--white)}
body{position:relative;font-family:"Alegreya",serif;color:var(--ink)}
.page{position:absolute;left:89px;top:425px;width:1044px;height:2280px;background:var(--white);box-shadow:0 0 24px rgba(0,0,0,.28)}
.abs{position:absolute}
/* header */
.header{left:0;top:0;width:1044px;height:71px;border-bottom:1px solid var(--line)}
.brand{left:56px;top:14px;display:flex;align-items:center;gap:8px}
.brand-dot{width:20px;height:20px;border-radius:50%;background:var(--lilac)}
.brand-name{font-size:22px;color:#c6889e;font-weight:400}
.brand-tag{left:86px;top:52px;font-size:6px;letter-spacing:1px;color:#b68a98;text-transform:uppercase}
.account{top:35px;left:716px;display:flex;gap:30px;font-size:9px;color:#333}
.account span{display:flex;align-items:center;gap:6px}
.nav{left:0;top:71px;width:1044px;height:51px;border-bottom:1px solid var(--pink)}
.nav a{position:absolute;top:20px;font-size:10px;color:#333;text-decoration:none}
/* title */
.title{left:0;width:1044px;top:175px;text-align:center;font-size:26px;font-weight:500}
.title-rule{left:444px;top:210px;width:110px;height:1px;background:#888}
/* sidebar */
.search-box{left:42px;top:268px;width:217px;height:30px;border:1px solid #ddd;font-family:"Alegreya SC",serif;font-size:9px;color:#999;padding:8px 9px;letter-spacing:.5px}
.search-btn{left:165px;top:311px;width:94px;height:24px;background:#242b2e;color:#fff;font-family:"Alegreya SC",serif;font-size:9px;text-align:center;line-height:24px;letter-spacing:.5px}
.filter-head{left:58px;top:363px;font-family:"Alegreya SC",serif;font-size:11px;font-weight:500}
.slider{left:53px;top:388px;width:92px;height:2px;background:var(--pink)}
.slider::before,.slider::after{content:"";position:absolute;top:-2px;width:5px;height:5px;border-radius:50%;background:var(--pink)}
.slider::after{right:0}
.range{left:58px;top:397px;font-family:"Alegreya SC",serif;font-size:11px}
.cats{left:52px;top:416px;list-style:none;font-size:7px;line-height:14.5px}
.cats li::before{content:"○ ";color:#bbb;font-size:5px}
.divider-v{left:278px;top:265px;width:1px;height:1500px;background:var(--pink)}
/* toolbar */
.rule-top{left:293px;top:253px;width:642px;height:1px;background:var(--pink)}
.rule-bot{left:293px;top:307px;width:642px;height:1px;background:var(--pink)}
.view{top:272px;width:37px;height:29px;border:1px solid var(--lilac);display:flex;align-items:center;justify-content:center}
/* products */
.card{width:205px}
.photo{position:relative;width:205px;height:206px}
.sale{position:absolute;left:8px;top:10px;width:65px;height:20px;background:var(--btn);color:#fff;font-family:"Montserrat",sans-serif;font-size:10px;line-height:20px;padding-left:13px}
.name{position:absolute;top:238px;width:205px;text-align:center;font-size:11px;font-weight:700}
.name.sc{font-family:"Alegreya SC",serif;font-weight:400;font-size:12px;letter-spacing:.4px}
.price{position:absolute;top:264px;width:205px;text-align:center;font-size:8px}
.price s{color:#999;margin-right:6px;font-size:6px}
.add{position:absolute;top:291px;left:50px;width:105px;height:24px;background:var(--btn);color:#fff;font-size:9px;text-align:center;line-height:24px;letter-spacing:.5px;font-family:"Alegreya SC",serif}
/* photo tones */
.ph-diamond{background:radial-gradient(ellipse 45% 40% at 35% 45%,#f4f4f4,transparent 70%),radial-gradient(ellipse 40% 40% at 70% 50%,#e6e6e6,transparent 70%),radial-gradient(circle at 50% 30%,#bdbcbc,#8f8c8c)}
.ph-silver{background:radial-gradient(circle at 50% 18%,#e9e6f5 0,transparent 22%),radial-gradient(circle at 50% 58%,#ffffff 0,#eef1f3 30%,#c6cfd4 55%,#8f9ca3 100%)}
.ph-rose{background:radial-gradient(ellipse 35% 40% at 38% 45%,#c6896d,transparent 70%),radial-gradient(ellipse 35% 40% at 66% 55%,#d6a086,transparent 70%),linear-gradient(135deg,#ecebee,#c9c6ca)}
.ph-pearl{background:radial-gradient(ellipse 35% 25% at 30% 45%,#d9d8d2,transparent 75%),radial-gradient(ellipse 35% 25% at 65% 55%,#cfcdc8,transparent 75%),linear-gradient(160deg,#6b6f72,#2a2e31)}
.ph-gem{background:radial-gradient(ellipse 12% 16% at 55% 48%,#c0702e,#8a6a34 60%,transparent 100%),radial-gradient(circle at 50% 40%,#f4f5f6,#c2c7cb)}
.ph-star{background:radial-gradient(ellipse 22% 20% at 32% 62%,#e3bf73,transparent 75%),radial-gradient(ellipse 20% 18% at 72% 40%,#e6c784,transparent 75%),linear-gradient(135deg,#f7dcd8,#efc4b8)}
.ph-stone{background:radial-gradient(ellipse 50% 30% at 50% 62%,#9cc7b9,transparent 80%),linear-gradient(160deg,#eef0ee,#cfd9d5)}
.ph-pendant{background:radial-gradient(circle at 55% 55%,#4e8a84 0,#8a8464 10%,#4c4b3c 28%,#141a3d 45%,#0f1535 100%)}
.ph-filigree{background:radial-gradient(ellipse 45% 35% at 55% 50%,#9b8e7c,transparent 75%),linear-gradient(150deg,#4d443b,#15110e)}
.ph-leather{background:radial-gradient(circle at 45% 42%,#d9e7ee 0,#7dc2db 22%,transparent 40%),linear-gradient(135deg,#e6a0ad 0,#c9b7c5 40%,#8fd0e6 100%)}
.ph-simple{background:radial-gradient(circle at 42% 42%,#f2efff 0,#d6d1f0 25%,transparent 42%),linear-gradient(160deg,#f0c4cd 0,#e9dfe6 45%,#9ed9df 100%)}
.ph-stylish{background:radial-gradient(circle at 50% 55%,#ffffff 0,#eef2f5 16%,transparent 30%),radial-gradient(ellipse 30% 40% at 78% 40%,#3aa9b5,transparent 70%),linear-gradient(140deg,#5c6a78,#a3adb6 55%,#d8cbc0)}
/* pagination */
.pager{top:1842px;left:794px;display:flex;gap:8px}
.pager span{width:26px;height:26px;border:1px solid #bbb;font-family:"Montserrat",sans-serif;font-size:13px;display:flex;align-items:center;justify-content:center}
/* newsletter & footer */
.footer{left:0;top:1971px;width:1044px;height:309px;background:var(--dark);color:#e9e9e9}
.news{left:119px;top:1917px;width:805px;height:80px;background:var(--pink);display:flex;align-items:center}
.news-title{margin-left:30px;color:#fbe8f2;font-size:17px;width:247px}
.news-input{width:354px;height:31px;background:#fff;font-family:"Montserrat",sans-serif;font-size:12px;color:#888;padding:8px 14px}
.news-btn{margin-left:13px;width:141px;height:31px;background:var(--lilac);color:#fff;font-family:"Montserrat",sans-serif;font-size:14px;text-align:center;line-height:31px}
.col-head{top:2058px;font-size:17px;color:#fff;text-decoration:underline;text-underline-offset:4px}
.col-text{font-size:10px;line-height:18px;letter-spacing:.6px;color:#ddd;white-space:nowrap}
.about-text{letter-spacing:1px}
.social{left:774px;top:2102px;display:flex;gap:18px}
.social i{display:block;width:12px;height:12px;border:1.5px solid #ddd;border-radius:3px}
.copy-rule{left:119px;top:2242px;width:805px;height:1px;background:#666}
.copy{left:0;width:1044px;top:2255px;text-align:center;font-size:10px;color:#ddd;letter-spacing:.3px}
</style>
</head>
<body>
<div class="page">
  <header class="abs header">
    <div class="abs brand"><span class="brand-dot"></span><span class="brand-name">Lumen Vale</span></div>
    <div class="abs brand-tag">fine jewelry store</div>
    <div class="abs account">
      <span><svg width="10" height="10" viewBox="0 0 10 10"><circle cx="5" cy="3" r="2.5" fill="#333"/><path d="M0 10c0-3 2-4.5 5-4.5S10 7 10 10z" fill="#333"/></svg>login</span>
      <span><svg width="12" height="10" viewBox="0 0 12 10"><path d="M6 10L1 5A2.8 2.8 0 016 1.5 2.8 2.8 0 0111 5z" fill="#333"/></svg>Favourite</span>
      <span><svg width="12" height="10" viewBox="0 0 12 10"><path d="M0 0h2l2 6h6l2-5H3" fill="none" stroke="#333" stroke-width="1.6"/><circle cx="5" cy="9" r="1" fill="#333"/><circle cx="9" cy="9" r="1" fill="#333"/></svg>cart</span>
    </div>
  </header>
  <nav class="abs nav">
    <a style="left:211px">Earrings</a><a style="left:317px">Rings</a><a style="left:404px">Topps</a>
    <a style="left:489px">Bracelate</a><a style="left:600px">Bindi</a><a style="left:685px">Watches</a>
  </nav>

  <h1 class="abs title">Shop Now</h1>
  <div class="abs title-rule"></div>

  <aside>
    <div class="abs search-box">SEARCH PRODUCTS</div>
    <div class="abs search-btn">SEARCH</div>
    <div class="abs filter-head">Filter by price</div>
    <div class="abs slider"></div>
    <div class="abs range">$1 to - 190</div>
    <ul class="abs cats"><li>Anklet</li><li>Belt buckle</li><li>Belly chain</li><li>Bindi</li><li>Bolo tie</li><li>Earrings</li><li>Watch</li><li>Necklace</li></ul>
  </aside>
  <div class="abs divider-v"></div>

  <div class="abs rule-top"></div>
  <div class="abs view" style="left:295px"><svg width="22" height="22" viewBox="0 0 22 22" fill="none" stroke="#d3a5cc"><rect x="1" y="1" width="9" height="9"/><rect x="12" y="1" width="9" height="9"/><rect x="1" y="12" width="9" height="9"/><rect x="12" y="12" width="9" height="9"/></svg></div>
  <div class="abs view" style="left:340px"><svg width="22" height="14" viewBox="0 0 22 14" stroke="#b98ac8" stroke-width="2"><path d="M1 2h2M6 2h15M1 7h2M6 7h15M1 12h2M6 12h15"/></svg></div>
  <div class="abs rule-bot"></div>

  <main>
    <div class="abs card" style="left:302px;top:315px"><div class="photo ph-diamond" role="img" aria-label="Photo of two silver diamond rings on fabric"><span class="sale">SALE!</span></div><div class="name">Diamond rings</div><div class="price"><s>$ 40.000</s>$ 35.000</div><div class="add">Add to cart</div></div>
    <div class="abs card" style="left:517px;top:315px"><div class="photo ph-silver" role="img" aria-label="Photo of a silver ring set with gems"><span class="sale">SALE!</span></div><div class="name">Silver Rings</div><div class="price"><s>$ 45.000</s>$ 35.000</div><div class="add">Add to cart</div></div>
    <div class="abs card" style="left:729px;top:315px"><div class="photo ph-rose" role="img" aria-label="Photo of two rose gold rings"><span class="sale">SALE!</span></div><div class="name">Artifical rings</div><div class="price"><s>$ 40.000</s>$ 35.000</div><div class="add">Add to cart</div></div>

    <div class="abs card" style="left:293px;top:708px"><div class="photo ph-pearl" role="img" aria-label="Photo of silver pearl earrings on dark wood"><span class="sale">SALE!</span></div><div class="name sc">Silver Earings</div><div class="price"><s>$ 45.000</s>$ 35.000</div><div class="add">Add to cart</div></div>
    <div class="abs card" style="left:513px;top:708px"><div class="photo ph-gem" role="img" aria-label="Photo of a golden earring with an orange gem"><span class="sale">SALE!</span></div><div class="name sc">Golden Earings</div><div class="price"><s>$ 45.000</s>$ 35.000</div><div class="add">Add to cart</div></div>
    <div class="abs card" style="left:729px;top:705px;width:222px"><div class="photo ph-star" role="img" aria-label="Photo of gold star earrings on pink" style="width:222px"><span class="sale">SALE!</span></div><div class="name sc" style="width:205px">Ring</div><div class="price" style="width:205px"><s>$ 45.000</s>$ 35.000</div><div class="add">Add to cart</div></div>

    <div class="abs card" style="left:293px;top:1100px"><div class="photo ph-stone" role="img" aria-label="Photo of a green stone necklace"><span class="sale">SALE!</span></div><div class="name">STONE NECKLACE</div><div class="price"><s>$ 45.000</s>$ 35.000</div><div class="add">Add to cart</div></div>
    <div class="abs card" style="left:514px;top:1100px"><div class="photo ph-pendant" role="img" aria-label="Photo of a golden pendant with a green stone on navy"><span class="sale">SALE!</span></div><div class="name">GOLDEN NECKLACE</div><div class="price"><s>$ 45.000</s>$ 35.000</div><div class="add">Add to cart</div></div>
    <div class="abs card" style="left:732px;top:1100px"><div class="photo ph-filigree" role="img" aria-label="Photo of a silver filigree necklace"><span class="sale">SALE!</span></div><div class="name">ARTIFICAL NECKLACE</div><div class="price"><s>$ 45.000</s>$ 35.000</div><div class="add">Add to cart</div></div>

    <div class="abs card" style="left:293px;top:1497px"><div class="photo ph-leather" role="img" aria-label="Photo of a blue leather strap watch"><span class="sale">SALE!</span></div><div class="name">Leather Watches</div><div class="price"><s>$ 45.000</s>$ 35.000</div><div class="add">Add to cart</div></div>
    <div class="abs card" style="left:511px;top:1497px"><div class="photo ph-simple" role="img" aria-label="Photo of a simple watch with a mint strap"><span class="sale">SALE!</span></div><div class="name">Simple Watch</div><div class="price"><s>$ 45.000</s>$ 35.000</div><div class="add">Add to cart</div></div>
    <div class="abs card" style="left:726px;top:1497px"><div class="photo ph-stylish" role="img" aria-label="Photo of a white watch with a bead bracelet on a wrist"><span class="sale">SALE!</span></div><div class="name">Stylish Watch</div><div class="price"><s>$ 45.000</s>$ 35.000</div><div class="add">Add to cart</div></div>
  </main>

  <div class="abs pager"><span>1</span><span>2</span><span>3</span><span><svg width="10" height="10" viewBox="0 0 10 10"><path d="M3 1l4 4-4 4" fill="none" stroke="#111" stroke-width="2"/></svg></span></div>

  <footer class="abs footer"></footer>
  <div class="abs news"><div class="news-title">Subscribe for Newsletter</div><div class="news-input">Your Email Address</div><div class="news-btn">Subscribe</div></div>

  <div class="abs col-head" style="left:144px">About Us</div>
  <p class="abs col-text about-text" style="left:140px;top:2106px">It is a long established fact that a<br>reader will be distracted by the<br>readable content of a page when<br>looking at its layout.</p>
  <div class="abs col-head" style="left:404px">Get in touch</div>
  <div class="abs col-text" style="left:404px;top:2103px">0800-555-0141</div>
  <div class="abs col-text" style="left:404px;top:2132px">020-55501872</div>
  <div class="abs col-text" style="left:404px;top:2164px">0800-555-0193</div>
  <div class="abs col-head" style="left:589px">Useful Links</div>
  <div class="abs col-text" style="left:587px;top:2099px;line-height:20px">Home<br>Products<br>service<br>Terms<br>FAQ</div>
  <div class="abs col-head" style="left:774px">Connect</div>
  <div class="abs" style="left:772px;top:2085px;font-size:6px;color:#ccc">Be apart of Lark Gems family</div>
  <div class="abs social"><i></i><i></i><i></i></div>
  <div class="abs copy-rule"></div>
  <div class="abs copy">© Copyright 2021 Lumen Vale. All Rights Reserved.</div>
</div>
</body>
</html>
```